Combining web page

We need a PSD webpage design for our PrestaShop store that shows food combining rules, you can see an example that we put here, you can follow the same information and food image combinations. You are just doing the design but the images when implemented on the website will be clickable that goes to product categories, all text and images will be editable.

This is just an example:
http://merrowtonic.com/content/7-food-combining-rules

Target Market(s)

Natural Product and supplement industry

Industry/Entity Type

Store

Number of Pages Required

1 page

Colors

Designer to choose colors to be used in the design.

Requirements
Must have
• 1. Clear images.
• 2. Clear readable text.
• 3. Company name shown Merrow Tonic.
• 4. Follow the food rules as seen on the web page example, but not the same design.
• 5. Logo should be seen.
• 7. All text and images will be editable.
• 8. Make sure the food images are in their proper groups.
• 9. You are not coping the design we gave you but the details have to be the same, copy the text and the image food groups are important, you cannot just put any food in a group, and the combinations are important.
Nice to have
• Here is the website it is for http://merrowtonic.com/

```html
<!DOCTYPE html>
<html lang="en">
<head>
<meta charset="utf-8">
<title>Food Combining Rules – Merrow Tonic</title>
<link rel="stylesheet" href="https://fonts.googleapis.com/css2?family=Lato:wght@400;700;900&family=Montserrat:wght@700;800&display=swap">
<style>
:root{
  --ink:#1d1d1f;
  --panel:#15171c;
  --page:#f1f1f1;
  --white:#ffffff;
  --muted:#8a8a8a;
  --orange:#f7a21b;
  --lime:#9ccc1c;
  --red:#ee3c48;
  --yellow:#fcb827;
  --blue:#1a5cb4;
  --pink:#ee6b73;
  --good-fill:#d8edb0;
  --good-line:#b7d97a;
  --fair-fill:#fde2a6;
  --fair-line:#f4c55c;
  --poor-fill:#f7b8ba;
  --poor-line:#e77d82;
  --footer:#1b1b1b;
}
*{box-sizing:border-box;margin:0;padding:0}
html,body{width:1200px;height:4486px;overflow:hidden}
body{position:relative;background:var(--page);font-family:'Lato',sans-serif;color:var(--ink)}
.abs{position:absolute}

/* header */
.site-header{left:0;top:0;width:1200px;height:120px;background:var(--white)}
.brand{left:60px;top:14px;display:flex;align-items:center;gap:10px;font:900 26px 'Lato',sans-serif;color:var(--ink)}
.brand-dot{width:16px;height:16px;border-radius:50%;background:var(--orange)}
.greeting{right:60px;top:22px;font:700 16px 'Lato',sans-serif;display:flex;gap:10px;align-items:center}
.main-nav{left:62px;top:82px;display:flex;gap:22px;font:700 17px 'Lato',sans-serif}
.search{left:925px;top:80px;width:130px;height:26px;border-bottom:1px solid #ccc;font-size:12px;color:var(--muted);padding:5px 0 0 22px}
.nav-icons{left:1075px;top:82px;display:flex;gap:14px}

/* hero */
.hero{left:0;top:120px;width:1200px;height:555px}
.hero-photo{position:absolute;inset:0;background:linear-gradient(180deg,#6b4a35 0%,#3a2a22 45%,#241a16 100%)}
.hero-title{left:250px;top:345px;font:400 50px 'Lato',sans-serif;color:var(--white)}
.filters{left:234px;top:425px;display:flex;gap:14px;align-items:flex-end}
.filter{width:195px;height:52px;background:var(--white);padding:6px 12px}
.filter small{display:block;font:700 11px 'Lato',sans-serif;color:var(--ink)}
.filter span{display:flex;justify-content:space-between;font-size:15px;color:var(--orange);margin-top:6px}
.find-btn{width:112px;height:42px;background:var(--orange);color:var(--white);font:700 15px 'Lato',sans-serif;display:flex;align-items:center;justify-content:center;margin-left:6px}

/* rules panel */
.rules-panel{left:243px;top:585px;width:717px;height:1745px;background:var(--panel)}
.rules-title{left:272px;top:605px;font:400 46px 'Lato',sans-serif;color:var(--white)}
.legend{left:804px;top:615px;font:700 9px 'Lato',sans-serif;color:var(--white);display:grid;grid-template-columns:auto auto;gap:6px 12px}
.legend i{display:inline-block;width:14px;height:14px;vertical-align:middle;margin-right:5px}

.group{position:absolute;left:0;width:1200px;height:420px}
.group-block{position:absolute;left:186px;top:114px;width:580px;height:294px}
.group-photo{position:absolute;left:204px;top:0;width:561px;height:369px;color:var(--white)}
.group-photo .fill{position:absolute;inset:0}
.group-name{position:absolute;left:45px;top:36px;font:400 40px 'Lato',sans-serif}
.group-sub{position:absolute;left:45px;top:80px;font:400 20px 'Lato',sans-serif}
.food-col{position:absolute;top:114px;font:400 14px/18px 'Lato',sans-serif;list-style:none}
.rule-card{position:absolute;left:600px;top:33px;width:459px;height:291px;background:var(--white);box-shadow:0 4px 12px rgba(0,0,0,.15)}
.rule-row{position:absolute;left:18px;display:flex;gap:0;height:84px;align-items:flex-start;padding:10px 12px;font:400 12px/14px 'Lato',sans-serif}
.rule-row div{width:104px}
.row-good{top:16px;width:426px;background:var(--good-fill);border:1px solid var(--good-line);color:#5c8a16}
.row-fair{top:106px;width:450px;background:var(--fair-fill);border:1px solid var(--fair-line);color:#c8851b}
.row-poor{top:196px;width:438px;background:var(--poor-fill);border:1px solid var(--poor-line);color:#b92b34}
.down-arrow{position:absolute;left:1040px;top:398px}

.more-btn{left:549px;top:2256px;width:102px;height:30px;background:#2b2d33;color:var(--white);font:700 11px 'Lato',sans-serif;display:flex;align-items:center;justify-content:center;gap:6px}

.meals{left:276px;top:2409px;width:723px;height:192px;background:#0f0f11;color:var(--white);display:flex;gap:48px;padding:22px 30px}
.meals h3{font:900 18px 'Lato',sans-serif;margin-bottom:2px}
.meals p{font:400 11.5px/15px 'Lato',sans-serif}

/* principles */
.principles-title{left:750px;top:2712px;font:900 80px/92px 'Lato',sans-serif;color:#d0d0d0}
.principle{position:absolute;width:342px;height:453px;color:var(--white);font:400 11.5px/15px 'Lato',sans-serif}
.principle .fill{height:220px}
.principle p{padding:22px 24px}
.p-green{left:72px;top:2796px;background:var(--lime)}
.p-blue{left:432px;top:2865px;background:var(--blue)}
.p-pink{left:789px;top:2925px;background:var(--pink)}

/* cookbook */
.cookbook{left:255px;top:3555px;width:195px;height:180px;background:#d5d5d5;padding:48px 0 0 36px}
.cookbook b{display:block;font:900 36px/40px 'Lato',sans-serif}
.cookbook span{font:400 14px 'Lato',sans-serif;letter-spacing:3px;color:#555}
.cookbook-text{left:480px;top:3594px;width:585px;font:400 12px/15px 'Lato',sans-serif;color:#333}

/* newsletter */
.newsletter{left:0;top:3885px;width:1200px;height:360px;background:var(--white)}
.news-title{left:0;top:3982px;width:1200px;text-align:center;font:800 28px 'Montserrat',sans-serif}
.news-sub{left:0;top:4030px;width:1200px;text-align:center;font:400 14px 'Lato',sans-serif;color:var(--muted)}
.news-input{left:315px;top:4089px;width:375px;height:36px;border-radius:18px;background:#ececec;font-size:12px;color:var(--muted);padding:11px 0 0 44px}
.news-btn{left:714px;top:4089px;width:186px;height:36px;border-radius:18px;background:#3ad17a;color:var(--white);font:800 12px 'Montserrat',sans-serif;display:flex;align-items:center;justify-content:center}

/* footer */
.site-footer{left:0;top:4245px;width:1200px;height:241px;background:var(--footer);color:var(--white)}
.ft-title{left:218px;top:4265px;font:900 16px 'Lato',sans-serif}
.ft-desc{left:218px;top:4288px;width:210px;font:700 11px/14px 'Lato',sans-serif}
.ft-more{left:218px;top:4320px;font:700 12px 'Lato',sans-serif;color:var(--orange)}
.ft-links{left:480px;top:4303px;display:flex;gap:40px;font:900 11px 'Lato',sans-serif;letter-spacing:1px}
.ft-social{left:1035px;top:4300px;display:flex;gap:18px}
.ft-social i{width:16px;height:16px;border-radius:50%;background:var(--white)}
.ft-copy{left:84px;top:4412px;font:400 11px 'Lato',sans-serif;color:#888}
.ft-legal{left:834px;top:4412px;display:flex;gap:44px;font:700 11px 'Lato',sans-serif;color:#bbb}
</style>
</head>
<body>

<header class="site-header abs">
  <div class="brand abs"><span class="brand-dot"></span>Merrow Tonic</div>
  <div class="greeting abs">
    <svg width="18" height="16" viewBox="0 0 18 16"><path d="M1 1h3l2 9h9l2-7H5" fill="none" stroke="#1d1d1f" stroke-width="2"/><circle cx="7" cy="14" r="1.5"/><circle cx="14" cy="14" r="1.5"/></svg>
    Hello, Rana!
  </div>
  <nav class="main-nav abs"><span>Our Products</span><span>Ingredients</span><span>Health Concerns</span><span>Blog</span><span>...</span></nav>
  <div class="search abs">Search store</div>
  <div class="nav-icons abs">
    <svg width="20" height="18"><path d="M2 3h16M2 9h16M2 15h16" stroke="#f7a21b" stroke-width="2"/></svg>
    <svg width="20" height="18"><path d="M2 2h16l-6 8v6l-4-2v-4z" fill="none" stroke="#f7a21b" stroke-width="2"/></svg>
  </div>
</header>

<section class="hero abs">
  <div class="hero-photo" role="img" aria-label="Table of traditional dishes in copper and clay bowls"></div>
</section>
<h1 class="hero-title abs">Ancient foods for todays’ lifestyle</h1>
<div class="filters abs">
  <div class="filter"><small>Meal Type</small><span>Lunch <b>▾</b></span></div>
  <div class="filter"><small>Select Dish/Cuisine</small><span>Chicken Biryani <b>▾</b></span></div>
  <div class="filter"><small>Food Type</small><span>Vegetables <b>▾</b></span></div>
  <div class="find-btn">⌕ Find Food</div>
</div>

<div class="rules-panel abs"></div>
<h2 class="rules-title abs">Food Combining Rules</h2>
<div class="legend abs">
  <span><i style="background:var(--lime)"></i>Combines well</span><span><i style="background:var(--yellow)"></i>Combine fair</span>
  <span><i style="background:var(--red)"></i>Combines poorly</span>
</div>

<!-- citrus -->
<section class="group" style="top:726px">
  <div class="group-block" style="background:var(--lime)"></div>
  <div class="group-photo">
    <div class="fill" role="img" aria-label="Halved citrus fruits and glasses of juice" style="background:linear-gradient(135deg,#5a4a2a,#b8862c 55%,#3a3020)"></div>
    <div class="group-name">Citrus</div><div class="group-sub">(Acid Fruits)</div>
    <ul class="food-col" style="left:57px"><li>Grapefruit</li><li>Oranges</li><li>Tangerine</li><li>Lemon</li><li>Lime</li><li>Cherry</li><li>Cranberry</li></ul>
    <ul class="food-col" style="left:171px"><li>Grapefruit</li><li>Oranges</li><li>Tangerine</li><li>Lemon</li><li>Lime</li><li>Cherry</li><li>Cranberry</li></ul>
    <ul class="food-col" style="left:288px"><li>Grapefruit</li><li>Oranges</li><li>Tangerine</li><li>Lemon</li><li>Lime</li><li>Cherry</li><li>Cranberry</li></ul>
  </div>
  <div class="rule-card">
    <div class="rule-row row-good"><div>Citrus (acid fruits)</div><div>Fruits (sub acid)</div><div>Neutral Fruits (nuts, seeds)</div><div>Greens</div></div>
    <div class="rule-row row-fair"><div>Sweet Fruits (palm fruits)</div><div>Starchy Vegetables</div><div>Melons</div><div>Grains</div></div>
    <div class="rule-row row-poor"><div>Dairy</div><div>Sucrolent Fruits (tomatoes)</div><div>Eggs, fats (nuts)</div><div>Vegetables (starchy, beans, etc)</div></div>
  </div>
  <svg class="down-arrow" width="20" height="24"><path d="M10 2v18M4 14l6 6 6-6" fill="none" stroke="#9a9a9a" stroke-width="1.5"/></svg>
</section>

<!-- fruits -->
<section class="group" style="top:1251px">
  <div class="group-block" style="background:var(--red)"></div>
  <div class="group-photo">
    <div class="fill" role="img" aria-label="Apples, bananas, cherries and guavas piled together" style="background:linear-gradient(135deg,#6a3a1e,#c28a2a 50%,#8a2a22)"></div>
    <div class="group-name">Fruits</div><div class="group-sub">(Sub Acid)</div>
    <ul class="food-col" style="left:57px"><li>Apples</li><li>Apricot</li><li>Banana</li><li>Cherries</li><li>Guava</li></ul>
    <ul class="food-col" style="left:171px"><li>Apples</li><li>Apricot</li><li>Banana</li><li>Cherries</li><li>Guava</li></ul>
    <ul class="food-col" style="left:288px"><li>Apples</li><li>Apricot</li><li>Banana</li><li>Cherries</li><li>Guava</li></ul>
  </div>
  <div class="rule-card">
    <div class="rule-row row-good"><div>Citrus (acid fruits)</div><div>Fruits (sub acid)</div><div>Sweet Fruits (palm fruits)</div><div>Greens</div></div>
    <div class="rule-row row-fair"><div>Eggs, fats (nuts)</div><div>Neutral Fruits</div><div>Melons</div><div>Grains</div></div>
    <div class="rule-row row-poor"><div>Eggs, nuts (dairy)</div><div>Sucrolent Fruits (tomatoes)</div><div>Vegetables (starchy, beans)</div><div></div></div>
  </div>
  <svg class="down-arrow" width="20" height="24"><path d="M10 2v18M4 14l6 6 6-6" fill="none" stroke="#9a9a9a" stroke-width="1.5"/></svg>
</section>

<!-- sweet fruits -->
<section class="group" style="top:1776px">
  <div class="group-block" style="background:var(--yellow)"></div>
  <div class="group-photo">
    <div class="fill" role="img" aria-label="Dried apricots, dates, figs and coconut" style="background:linear-gradient(135deg,#2a1e14,#6a4a28 55%,#3a2a1a)"></div>
    <div class="group-name">Sweet Fruits</div><div class="group-sub">(Palm Fruits)</div>
    <ul class="food-col" style="left:57px"><li>Apricot (dried)</li><li>Banana (dried)</li><li>Coconut</li><li>Currants (dried)</li><li>Dates</li><li>Figs (dried)</li><li>Peaches (dried)</li><li>Pears (dried)</li></ul>
    <ul class="food-col" style="left:171px"><li>Apricot (dried)</li><li>Banana (dried)</li><li>Coconut</li><li>Currants (dried)</li><li>Dates</li><li>Figs (dried)</li><li>Peaches (dried)</li><li>Pears (dried)</li></ul>
    <ul class="food-col" style="left:288px"><li>Apricot (dried)</li><li>Banana (dried)</li><li>Coconut</li><li>Currants (dried)</li><li>Dates</li><li>Figs (dried)</li><li>Peaches (dried)</li><li>Pears (dried)</li></ul>
  </div>
  <div class="rule-card">
    <div class="rule-row row-good"><div>Citrus (acid fruits)</div><div>Fruits (sub acid)</div><div>Sweet Fruits (palm fruits)</div><div>Greens</div></div>
    <div class="rule-row row-fair"><div>Vegetables (starchy)</div><div>Grains</div><div>Melons</div><div>Celery</div></div>
    <div class="rule-row row-poor"><div>Dairy</div><div>Sucrolent Fruits (tomatoes)</div><div>Eggs, fats (nuts)</div><div>Vegetables (beans, etc)</div></div>
  </div>
  <svg class="down-arrow" width="20" height="24"><path d="M10 2v18M4 14l6 6 6-6" fill="none" stroke="#9a9a9a" stroke-width="1.5"/></svg>
</section>

<div class="more-btn abs">↻ Find more...</div>

<section class="meals abs">
  <div><h3>Breakfast</h3><p>Start the day with acid or sub acid fruits eaten alone, then wait a while before grains. Fresh citrus with greens keeps digestion light, and dried sweet fruits go best with other fruit rather than dairy or nuts. Keep portions small, drink water first and give each meal time before the next one arrives.</p></div>
  <div><h3>Dinner</h3><p>Pair starchy vegetables with greens, or a protein with greens, but keep starch and protein apart. Leave fruit out of the evening meal, choose gentle cooked grains, and finish eating early enough to rest. Simple plates with few foods combine best and leave the body calm through the night.</p></div>
</section>

<h2 class="principles-title abs">Principles<br>of Eating</h2>
<article class="principle p-green">
  <div class="fill" role="img" aria-label="Green salad ingredients on a board" style="background:linear-gradient(160deg,#8ab81a,#5f8a10)"></div>
  <p>Eat fresh whole foods in simple combinations. Greens go well with almost everything, so build each plate around them and add one main food. Fruits digest quickly and are best eaten alone or with other fruit of the same group. Chew slowly, eat when calm and stop before you feel full. Seasonal produce carries the most flavour and goodness, and a short list of foods per meal lets digestion work well without strain.</p>
</article>
<article class="principle p-blue">
  <div class="fill" role="img" aria-label="Hands preparing food on a blue table" style="background:linear-gradient(160deg,#2a6cc4,#113f86)"></div>
  <p>Drink water between meals rather than with them so digestion stays strong. Avoid mixing heavy proteins with heavy starches on one plate. Let sweet fruits stand as a snack, and keep melons on their own. Cooked grains pair gently with vegetables. Listen to your hunger, keep regular meal times and choose foods that leave you light, clear and full of steady energy all day long.</p>
</article>
<article class="principle p-pink">
  <div class="fill" role="img" aria-label="Bowl of fresh berries and yoghurt" style="background:linear-gradient(160deg,#f08a90,#d9505a)"></div>
  <p>Traditional kitchens teach balance: a little of each taste, plenty of greens and food prepared with care. Combine acid fruits with sub acid fruits, sweet with sub acid, and keep dairy simple. Rest after eating, share meals with others and enjoy the ritual. Small daily habits like these build lasting health and a happy gut over the years.</p>
</article>

<div class="cookbook abs"><b>Nine<br>Harvests</b><span>COOKBOOK</span></div>
<p class="cookbook-text abs">A family cookbook of whole food recipes built on the combining rules above. Each chapter groups dishes by the foods they share, from citrus breakfasts and fruit bowls to grain suppers and green soups. Clear notes explain which foods combine well, which combine fairly and which to keep apart, so you can plan a week of meals with ease. Simple steps, short lists and honest ingredients make it a friendly guide for new cooks and old hands alike, with tips for shopping, storing and preparing produce at its best.</p>

<section class="newsletter abs"></section>
<h2 class="news-title abs">Subscribe To Our Newsletters</h2>
<p class="news-sub abs">You may unsubscribe at any moment. For that purpose please find our contact info in the legal notice.</p>
<div class="news-input abs">name@mail.com</div>
<div class="news-btn abs">GET STARTED</div>

<footer class="site-footer abs">
  <svg class="abs" style="left:178px;top:30px" width="30" height="44" viewBox="0 0 30 44"><path d="M4 2v12M8 2v12M12 2v12M4 14h8M8 14v28M24 2c-4 4-4 14 0 16v24" fill="none" stroke="#f7a21b" stroke-width="3"/></svg>
</footer>
<div class="ft-title abs">FOOD DELIVERY</div>
<div class="ft-desc abs">Everything from your kitchen, delivered fresh to your door</div>
<div class="ft-more abs">Learn more</div>
<nav class="ft-links abs"><span>SECURE PAYMENT</span><span>TEAM</span><span>ABOUT US</span><span>CONTACTS</span></nav>
<div class="ft-social abs"><i></i><i></i><i></i></div>
<div class="ft-copy abs">© 2024 Merrow Tonic. All rights reserved.</div>
<div class="ft-legal abs"><span>PRIVACY POLICY</span><span>TERMS AND CONDITIONS</span></div>

</body>
</html>
```